Re-Design the flow of the Orvane Framework

The orvane framework is a 10 step model that helps teams/organizations become high performing. Attached the model which i created. I love the design as it is but i used a template i don't owe the rights of so i would like to use this platform to see what you can come up with the redesign this flow while keeping the key elements in place. I like the flow, i like the cleanness and i like it to be compact.

Target Market(s)

Organizational change / Leadership/ Consultancy

Industry/Entity Type

Leadership

Requirements
Must have
• Keep as much as possible the flow and feel of the attached
Nice to have
• -Maybe some twist in how the different parts connect (not a must)
Should not have
• Less or more steps than added in the attached file

```html
<!DOCTYPE html>
<html lang="en">
<head>
<meta charset="utf-8">
<title>The Orvane Framework</title>
<link href="https://fonts.googleapis.com/css2?family=Oswald:wght@300;400;500;600;700&display=swap" rel="stylesheet">
<style>
  :root {
    --bg: #fbfbfb;
    --ink: #3a3a3a;
    --white: #ffffff;

    --lime: #8cc63f;
    --green: #39b54a;
    --forest: #0f9447;
    --sky: #1a75bc;
    --indigo: #283a93;
    --navy: #262262;
    --violet: #662d91;
    --plum: #82288f;
    --wine: #9e1f63;
    --raspberry: #d4145a;
    --orchid: #92278f;
    --orange: #f15a29;
    --pink: #d81b60;

    --tint-cool: #eef4ee;
    --tint-warm: #f6eef5;
    --band-start: #5bb947;
    --band-end: #d7df23;
    --box-green: #3aaa49;
  }

  * { box-sizing: border-box; }

  html, body {
    margin: 0;
    padding: 0;
    width: 1200px;
    height: 848px;
    overflow: hidden;
    background: var(--bg);
  }

  .poster {
    width: 1200px;
    height: 848px;
    background: radial-gradient(ellipse at 45% 40%, #ffffff 0%, #ffffff 45%, #ececec 100%);
  }

  .flow { display: block; width: 1200px; height: 848px; }

  .step-text {
    font-family: "Oswald", sans-serif;
    font-weight: 300;
    font-size: 16px;
    fill: var(--ink);
  }

  .hub-text {
    font-family: "Oswald", sans-serif;
    font-weight: 500;
    font-size: 17px;
    fill: var(--white);
    text-anchor: middle;
  }

  .phase-label {
    font-family: "Oswald", sans-serif;
    font-weight: 700;
    font-size: 15px;
    letter-spacing: 2.5px;
  }
  .phase-label--self { fill: var(--green); }
  .phase-label--human { fill: var(--indigo); }
  .phase-label--engage { fill: var(--wine); }

  .goal-title {
    font-family: "Oswald", sans-serif;
    font-weight: 600;
    font-size: 18px;
    fill: var(--white);
    text-anchor: middle;
  }

  .goal-item {
    font-family: "Oswald", sans-serif;
    font-weight: 400;
    font-size: 14.5px;
    fill: var(--white);
  }

  .start-text {
    font-family: "Oswald", sans-serif;
    font-weight: 500;
    font-size: 34px;
    fill: var(--white);
  }

  .brand-title {
    font-family: "Oswald", sans-serif;
    font-weight: 600;
    font-size: 56px;
    letter-spacing: 3px;
    fill: var(--white);
  }

  .brand-tagline {
    font-family: "Oswald", sans-serif;
    font-weight: 500;
    font-size: 20px;
    letter-spacing: 1.2px;
    fill: var(--white);
  }

  .track { fill: none; stroke: url(#trackGradient); stroke-width: 18; }
  .start-track { fill: none; stroke: var(--lime); stroke-width: 18; }
  .node { stroke: var(--white); stroke-width: 4; filter: drop-shadow(0 2px 3px rgba(0,0,0,0.2)); }
  .hub { stroke: var(--white); stroke-width: 6; filter: drop-shadow(0 4px 8px rgba(0,0,0,0.2)); }
  .icon { fill: var(--white); }
  .icon-line { fill: none; stroke: var(--white); stroke-width: 3; stroke-linecap: round; stroke-linejoin: round; }
  .raised { filter: drop-shadow(2px 4px 6px rgba(0,0,0,0.18)); }
</style>
</head>
<body>
<main class="poster">
  <svg class="flow" viewBox="0 0 1200 848" xmlns="http://www.w3.org/2000/svg" aria-labelledby="flowTitle">
    <title id="flowTitle">The Orvane Framework – ten steps from self direction to reaching full potential</title>
    <defs>
      <linearGradient id="trackGradient" gradientUnits="userSpaceOnUse" x1="150" y1="0" x2="960" y2="0">
        <stop offset="0" stop-color="var(--lime)"/>
        <stop offset="0.2" stop-color="var(--green)"/>
        <stop offset="0.35" stop-color="var(--sky)"/>
        <stop offset="0.5" stop-color="var(--navy)"/>
        <stop offset="0.65" stop-color="var(--violet)"/>
        <stop offset="0.85" stop-color="var(--wine)"/>
        <stop offset="1" stop-color="var(--raspberry)"/>
      </linearGradient>
      <linearGradient id="riseGradient" x1="0" y1="1" x2="0" y2="0">
        <stop offset="0" stop-color="var(--raspberry)"/>
        <stop offset="1" stop-color="var(--orange)"/>
      </linearGradient>
      <linearGradient id="cardGradient" x1="0" y1="0" x2="0" y2="1">
        <stop offset="0" stop-color="var(--orange)"/>
        <stop offset="1" stop-color="var(--pink)"/>
      </linearGradient>
      <linearGradient id="hubCoolGradient" x1="0" y1="0" x2="1" y2="1">
        <stop offset="0" stop-color="var(--sky)"/>
        <stop offset="1" stop-color="var(--navy)"/>
      </linearGradient>
      <linearGradient id="hubWarmGradient" x1="0" y1="0" x2="1" y2="1">
        <stop offset="0" stop-color="var(--orchid)"/>
        <stop offset="1" stop-color="var(--wine)"/>
      </linearGradient>
      <linearGradient id="bandGradient" x1="0" y1="0" x2="1" y2="0">
        <stop offset="0" stop-color="var(--band-start)"/>
        <stop offset="1" stop-color="var(--band-end)"/>
      </linearGradient>

      <path id="phaseSelfPath" d="M230,400 A130,130 0 0 1 360,270"/>
      <path id="phaseHumanPath" d="M360,270 A130,130 0 0 1 490,400"/>
      <path id="phaseEngagePath" d="M618,400 A142,142 0 0 0 902,400"/>
    </defs>

    <!-- loop tints -->
    <circle cx="360" cy="400" r="182" fill="var(--tint-cool)"/>
    <circle cx="760" cy="400" r="182" fill="var(--tint-warm)"/>

    <!-- continuous track -->
    <path class="start-track" d="M160,604 V400"/>
    <path class="track" d="M160,400 A200,200 0 0 1 560,400 A200,200 0 0 0 960,400"/>
    <rect x="951" y="132" width="18" height="270" fill="url(#riseGradient)"/>
    <polygon points="960,62 924,136 996,136" fill="var(--orange)"/>

    <g class="icon-line">
      <polyline points="154,548 160,541 166,548"/>
      <polyline points="154,526 160,519 166,526"/>
      <polyline points="154,504 160,497 166,504"/>
    </g>

    <!-- phase labels -->
    <text class="phase-label phase-label--self"><textPath href="#phaseSelfPath" startOffset="50%" text-anchor="middle">SELF DIRECTION</textPath></text>
    <text class="phase-label phase-label--human"><textPath href="#phaseHumanPath" startOffset="50%" text-anchor="middle">HUMAN EXPERIENCE</textPath></text>
    <text class="phase-label phase-label--engage"><textPath href="#phaseEngagePath" startOffset="50%" text-anchor="middle">UNLEASH ENGAGEMENT</textPath></text>

    <!-- hubs -->
    <circle class="hub" cx="360" cy="400" r="88" fill="url(#hubCoolGradient)"/>
    <text class="hub-text" x="360" y="380">CAPABILITIES</text>
    <text class="hub-text" x="360" y="404">DRIVING A SOLID</text>
    <text class="hub-text" x="360" y="428">FOUNDATION</text>

    <circle class="hub" cx="760" cy="400" r="88" fill="url(#hubWarmGradient)"/>
    <text class="hub-text" x="760" y="380">CAPABILITIES</text>
    <text class="hub-text" x="760" y="404">MAXIMIZING</text>
    <text class="hub-text" x="760" y="428">EXCELLENCE</text>

    <!-- step nodes -->
    <g class="steps">
      <g transform="translate(166.8,348.2)">
        <circle class="node" r="24" fill="var(--lime)"/>
        <circle class="icon-line" r="9"/><circle class="icon" r="4"/>
        <path class="icon-line" d="M0,-14 V-11 M0,11 V14 M-14,0 H-11 M11,0 H14"/>
      </g>
      <g transform="translate(218.6,258.6)">
        <circle class="node" r="24" fill="var(--green)"/>
        <circle class="icon" cx="-3" cy="-6" r="5.5"/>
        <path class="icon" d="M-12,10 A9.5,9 0 0 1 7,10 Z"/>
        <path class="icon-line" d="M9,2 V10 M5,6 H13" stroke-width="2.5"/>
      </g>
      <g transform="translate(308.2,206.8)">
        <circle class="node" r="24" fill="var(--forest)"/>
        <rect class="icon" x="-11" y="-9" width="4.5" height="4.5"/><rect class="icon" x="-3" y="-8.5" width="14" height="3.5"/>
        <rect class="icon" x="-11" y="-2" width="4.5" height="4.5"/><rect class="icon" x="-3" y="-1.5" width="14" height="3.5"/>
        <rect class="icon" x="-11" y="5" width="4.5" height="4.5"/><rect class="icon" x="-3" y="5.5" width="14" height="3.5"/>
      </g>
      <g transform="translate(411.8,206.8)">
        <circle class="node" r="24" fill="var(--sky)"/>
        <path class="icon-line" d="M-5,-2 V-7 A5,5 0 0 1 5,-7 V-2"/>
        <rect class="icon" x="-9" y="-3" width="18" height="14" rx="2.5"/>
      </g>
      <g transform="translate(501.4,258.6)">
        <circle class="node" r="24" fill="var(--indigo)"/>
        <rect class="icon" x="-5" y="-12" width="6" height="16" rx="3"/>
        <rect class="icon" x="-7" y="-1" width="16" height="12" rx="4"/>
      </g>
      <g transform="translate(553.2,348.2)">
        <circle class="node" r="24" fill="var(--navy)"/>
        <path class="icon-line" d="M-5,-2 V-8 A5,5 0 0 1 5,-8 V-6"/>
        <rect class="icon" x="-9" y="-3" width="18" height="14" rx="2.5"/>
      </g>
      <g transform="translate(575.2,476.6)">
        <circle class="node" r="24" fill="var(--violet)"/>
        <path class="icon" d="M-12,-1 A12,9 0 1 1 -3,8 L-10,11 L-8,5 A12,9 0 0 1 -12,-1 Z"/>
      </g>
      <g transform="translate(683.5,584.8)">
        <circle class="node" r="24" fill="var(--plum)"/>
        <polygon class="icon" points="3,-13 -9,2 -1,2 -4,13 9,-3 1,-3"/>
      </g>
      <g transform="translate(836.5,584.8)">
        <circle class="node" r="24" fill="var(--wine)"/>
        <circle class="icon" cx="-6" cy="-6" r="4.5"/><circle class="icon" cx="6" cy="-6" r="4.5"/>
        <path class="icon" d="M-13,9 V5 A6,5.5 0 0 1 -1,5 V9 Z"/><path class="icon" d="M1,9 V5 A6,5.5 0 0 1 13,5 V9 Z"/>
      </g>
      <g transform="translate(944.8,476.6)">
        <circle class="node" r="24" fill="var(--raspberry)"/>
        <circle class="icon-line" cx="-3" cy="-3" r="7"/>
        <path class="icon-line" d="M3,3 L10,10" stroke-width="4"/>
      </g>
    </g>

    <!-- step copy -->
    <g class="step-copy">
      <text class="step-text" text-anchor="end"><tspan x="122" y="315">Discover</tspan><tspan x="122" y="333">your purpose.</tspan><tspan x="122" y="351">Why do</tspan><tspan x="122" y="369">you exist?</tspan></text>
      <text class="step-text" text-anchor="end"><tspan x="186" y="196">Identify</tspan><tspan x="186" y="214">purpose</tspan><tspan x="186" y="232">activators</tspan><tspan x="186" y="250">(Vision)</tspan></text>
      <text class="step-text" text-anchor="middle"><tspan x="296" y="116">Develop a</tspan><tspan x="296" y="134">master plan</tspan><tspan x="296" y="152">(strategy)</tspan></text>
      <text class="step-text" text-anchor="middle"><tspan x="424" y="98">Cultivate a</tspan><tspan x="424" y="116">psychological</tspan><tspan x="424" y="134">safety and</tspan><tspan x="424" y="152">ownership</tspan></text>
      <text class="step-text"><tspan x="534" y="196">Tap into peoples</tspan><tspan x="534" y="214">purpose &amp; passion</tspan><tspan x="534" y="232">(intrinsic</tspan><tspan x="534" y="250">motivation)</tspan></text>
      <text class="step-text"><tspan x="598" y="314">Unlock culture</tspan><tspan x="598" y="332">of personal</tspan><tspan x="598" y="350">growth &amp;</tspan><tspan x="598" y="368">Development</tspan></text>
      <text class="step-text" text-anchor="end"><tspan x="532" y="482">Prioritize</tspan><tspan x="532" y="500">feedback &amp;</tspan><tspan x="532" y="518">transparency</tspan></text>
      <text class="step-text" text-anchor="end"><tspan x="666" y="640">Empower</tspan><tspan x="666" y="658">the community</tspan><tspan x="666" y="676">from bottom-up</tspan></text>
      <text class="step-text"><tspan x="854" y="640">Put excellent</tspan><tspan x="854" y="658">(team) performance</tspan><tspan x="854" y="676">in the spotlight</tspan></text>
      <text class="step-text"><tspan x="988" y="482">Monitor</tspan><tspan x="988" y="500">engagement</tspan><tspan x="988" y="518">Real-Time</tspan></text>
    </g>

    <!-- outcome card -->
    <g class="outcome">
      <rect class="raised" x="1000" y="130" width="185" height="312" rx="16" fill="url(#cardGradient)"/>
      <text class="goal-title" x="1092.5" y="166">REACHING FULL</text>
      <text class="goal-title" x="1092.5" y="190">POTENTIAL OF PEOPLE</text>
      <text class="goal-title" x="1092.5" y="214">AND ORGANIZATION</text>
      <circle class="icon" cx="1018" cy="247" r="3"/>
      <text class="goal-item"><tspan x="1028" y="252">PRODUCTIVITY</tspan><tspan x="1028" y="270">UP TO 800%</tspan></text>
      <circle class="icon" cx="1018" cy="299" r="3"/>
      <text class="goal-item"><tspan x="1028" y="304">EMPLOYEE</tspan><tspan x="1028" y="322">ENGAGEMENT &gt;90%</tspan></text>
      <circle class="icon" cx="1018" cy="351" r="3"/>
      <text class="goal-item"><tspan x="1028" y="356">MAX DISCRETIONARY</tspan><tspan x="1028" y="374">EFFORT GAP</tspan></text>
      <circle class="icon" cx="1018" cy="403" r="3"/>
      <text class="goal-item"><tspan x="1028" y="408">HIGH RESILIENCE</tspan><tspan x="1028" y="426">TO CHANGE</tspan></text>
    </g>

    <!-- start box -->
    <g class="start">
      <rect class="raised" x="40" y="598" width="250" height="110" rx="14" fill="var(--box-green)"/>
      <text class="start-text" x="60" y="643">(RE)START HERE</text>
      <text class="start-text" x="60" y="688">(RE)INVENT HERE</text>
    </g>

    <!-- brand band -->
    <g class="brand-band">
      <rect x="0" y="740" width="1200" height="108" fill="url(#bandGradient)"/>
      <text class="brand-title" x="40" y="816">THE ORVANE FRAMEWORK</text>
      <text class="brand-tagline" x="720" y="790">LIBERATE THE WORKUNLEASHING THROUGH</text>
      <text class="brand-tagline" x="720" y="815">PURPOSE AT EVERY LEVEL OF SCALE</text>
    </g>
  </svg>
</main>
</body>
</html>
```